TallFern's Bold New Thank You Greeting Card 2.0

We want an updated thank you card design that is creative and clever. Same dimensions as the TF_ThankYouCard uploaded below: a half-fold card that fits in a 4 3/8 x 5 3/4" envelope. Looking for design styles that are minimalist, with themes that are bold and playful. Attached files show past designs we have used, but we are looking for something more memorable, while maintaining the same color scheme and fundamental elements of our logo. Additional design examples for reference here: https://www.pinboardly.example/iamgavinwhelk/logo-inspiration/
Updates

Based on the designs I've received so far, I realized I was not clear enough in my original brief. I want it to be a THANK YOU CARD first and foremost, and promotion of our company should appear as secondary afterthought. The front should either say "thank you", or could have a completely unique design without text, but must be WITHOUT our name and logo. I don't want the reader to know who it is from until they open it. There could be hints of who it is from, by incorporating our colors, fonts or the bird element, but our logo should be on the inside or back only. I want a design that includes front, inside and back, but initial submissions can focus on the front design if that's easier. Most of the designs submitted don't follow all the parameters of the brief, so if you go back and read the brief carefully, it should be easy to stand out and win!

Project Deadline Extended
Reason: Because I had to clarify project details and remind designers to read my brief carefully, I believe a few more days will bring a better variety of high quality designs closely aligned with what I'm looking for.

Target Market(s)

Our clients and potential clients. Local Portland OR market. Hipsters, professionals, multi-generational.

Industry/Entity Type

Real Estate

Font styles to use
Sans Serif

Colors
0292cd
ffffff
1b1b1b

Requirements
Must have
• Clever, memorable design that stands out.
• We want to REINVENT our current thank you card. (Attached) I want it to be a THANK YOU CARD first and foremost, and promotion of our company should appear as secondary afterthought.
• The front should either say "thank you", or could have a completely unique design without text, but must be WITHOUT our name and logo. I don't want the reader to know who it is from until they open it. There could be hints of who it is from, by incorporating our colors, fonts or the bird element, but our logo should be on the inside or back only.
• For more info on our companies, go here: http://mytallfern.example
• Also see style guide in attached files.
Nice to have
• Could have a completely different style than the designs I uploaded, but must tie into some elements of our logo. You could add colors as long as they play well with our existing palette. You can break up any elements of our logo and text that you want to create your design.
• Doesn't have to, but any reflection or incorporation of our Core Values (below) would be a bonus:
• TALLFERNS ARE:
• Leaders – We bravely seize opportunity and dare to do things differently.
• Listeners – We practice agenda-free listening.
• Creators – We solve instead of sell.
• Educators – We teach and empower openly and honestly.
• Givers – We exceed expectations and deliver with generosity.
Should not have
• Should not be so silly or playful that it comes across as insincere or irreverent. Don't submit business card designs. I'm only interested in unique and original artwork. Don't just submit a design with our logo and a border on a card.

```html
<!DOCTYPE html>
<html lang="en">
<head>
<meta charset="UTF-8">
<title>TallFern Thank You Card</title>
<link rel="stylesheet" href="https://fonts.googleapis.com/css2?family=Montserrat:wght@400;700&display=swap">
<style>
  :root {
    --backdrop: #a4a4a4;
    --card-white: #ffffff;
    --brand-blue: #0292cd;
    --brand-grey: #8a8a8e;
    --card-blue: #0583c3;
    --ornament-blue: #62aedc;
    --ornament-grey: #d3d3d3;
    --ink-white: #ffffff;
  }
  html, body {
    margin: 0;
    padding: 0;
    width: 1200px;
    height: 1200px;
    overflow: hidden;
    background: var(--backdrop);
  }
  .canvas {
    position: relative;
    width: 1200px;
    height: 1200px;
  }
  .card {
    position: absolute;
    overflow: hidden;
  }
  .card-back {
    left: 203px;
    top: 117px;
    width: 618px;
    height: 383px;
    background: var(--card-white);
  }
  .brand-mark {
    position: absolute;
    left: 226px;
    top: 66px;
    width: 164px;
    height: 164px;
    background: var(--brand-grey);
  }
  .brand-name {
    position: absolute;
    left: 0;
    top: 252px;
    width: 470px;
    text-align: right;
    font-family: "Montserrat", sans-serif;
    font-weight: 700;
    font-size: 78px;
    letter-spacing: -3px;
    line-height: 1;
    color: var(--brand-blue);
  }
  .branch-corner {
    position: absolute;
    left: 438px;
    top: 0;
    width: 165px;
    height: 258px;
    border-radius: 0 0 60px 90px;
    background: linear-gradient(200deg, var(--ornament-grey), rgba(211,211,211,0.25));
  }
  .card-front {
    left: 514px;
    top: 558px;
    width: 620px;
    height: 384px;
    background: var(--card-blue);
  }
  .ornament {
    position: absolute;
    background: var(--ornament-blue);
    opacity: 0.75;
  }
  .bird-top { left: 246px; top: 16px; width: 66px; height: 74px; border-radius: 50%; }
  .bird-left { left: 36px; top: 212px; width: 70px; height: 70px; border-radius: 50%; }
  .bird-right { left: 512px; top: 236px; width: 66px; height: 76px; border-radius: 50%; }
  .branch-top-right {
    left: 440px; top: 0; width: 180px; height: 140px;
    border-radius: 0 0 0 90px;
    background: linear-gradient(210deg, var(--ornament-blue), rgba(98,174,220,0.2));
  }
  .branch-bottom-left {
    left: 0; top: 212px; width: 286px; height: 172px;
    border-radius: 0 120px 0 0;
    background: linear-gradient(30deg, var(--ornament-blue), rgba(98,174,220,0.15));
  }
  .greeting {
    position: absolute;
    margin: 0;
    font-family: "Montserrat", sans-serif;
    font-weight: 400;
    font-size: 60px;
    letter-spacing: -1px;
    color: var(--ink-white);
    line-height: 1;
  }
  .greeting-thank { left: 136px; top: 124px; }
  .greeting-you { left: 298px; top: 218px; }
</style>
</head>
<body>
<main class="canvas">
  <section class="card card-back">
    <div class="branch-corner" role="img" aria-label="Grey leafy branch ornament"></div>
    <div class="brand-mark" aria-hidden="true"></div>
    <div class="brand-name">tallfern</div>
  </section>

  <section class="card card-front">
    <div class="ornament branch-top-right" role="img" aria-label="Light blue leafy branch ornament"></div>
    <div class="ornament branch-bottom-left" role="img" aria-label="Light blue leafy branch ornament"></div>
    <div class="ornament bird-top" role="img" aria-label="Light blue bird silhouette in flight"></div>
    <div class="ornament bird-left" role="img" aria-label="Light blue bird silhouette in flight"></div>
    <div class="ornament bird-right" role="img" aria-label="Light blue bird silhouette in flight"></div>
    <p class="greeting greeting-thank">Thank</p>
    <p class="greeting greeting-you">You</p>
  </section>
</main>
</body>
</html>
```